Pebblewick - a new nut butter brand in Switzerland

We are launching a new and innovative line of organic Nut Butters in Switzerland called Pebblewick. 340g round glass jar and require a cool label design for the front, back and top of the jar. Pebblewick soldier and our slogan is "Kernels from every far corner - stirred in Zurich". It must therefore include the "flavor". The back label wants to include product description and nutritional information. The top should include the brand name, flavor and maybe another image. Overall we want to convey a young and fun designs appealing to the local hipster movement. The label designs we like are Fennimore's Spread, Ottilie's and Mango Ritual.

Target Market(s)

Swiss hipster commutity

Industry/Entity Type

Food Production

Font styles to use
Sans Serif

Colors
85cae6
86cfc6
cadf82
fbf289
fee18a
f8ba93
f9ba93
f59296
eea4c8

Requirements
Must have
• "Almond butter" on the front. A graphic representation of a nut cracker that will serve as our logo - clean and fun (refer to mango ritual) in large font "Kernels from every far corner - stirred in Zurich" on the front; slightly smaller than the "Almond Butter"
Nice to have

```html
<!DOCTYPE html>
<html lang="en">
<head>
<meta charset="utf-8">
<title>Pebblewick Almond Butter – Back Label</title>
<link href="https://fonts.googleapis.com/css2?family=Montserrat:wght@600;700&family=Questrial&display=swap" rel="stylesheet">
<style>
  :root {
    --ink: #111111;
    --cell: #ffffff;
    --label-grey: #a3a4a7;
    --figure-grey: #8f9094;
    --almond-light: #dccaa9;
    --almond-mid: #d2bc97;
    --almond-deep: #c8b08b;
    --sky: #85cae6;
    --mint: #86cfc6;
    --lime: #cadf82;
    --lemon: #fbf289;
    --peach: #f8ba93;
    --rose: #f59296;
    --lilac: #eea4c8;
  }
  html, body {
    margin: 0;
    padding: 0;
    overflow: hidden;
  }
  .label {
    position: relative;
    width: 1200px;
    height: 962px;
    overflow: hidden;
    font-family: "Questrial", sans-serif;
    color: var(--ink);
  }
  .label__backdrop {
    position: absolute;
    inset: 0;
    background: radial-gradient(ellipse at 50% 40%, var(--almond-light) 0%, var(--almond-mid) 60%, var(--almond-deep) 100%);
  }
  .label__band {
    position: absolute;
    left: 0;
    width: 100%;
    height: 10px;
    background: linear-gradient(90deg, var(--sky), var(--mint), var(--lime), var(--lemon), var(--peach), var(--rose), var(--lilac));
  }
  .label__band--top { top: 0; }
  .label__band--bottom { bottom: 0; }
  .brand {
    position: absolute;
    top: 44px;
    left: 0;
    width: 100%;
    display: flex;
    align-items: center;
    justify-content: center;
    gap: 12px;
    margin: 0;
    font-family: "Montserrat", sans-serif;
    font-weight: 700;
    font-size: 30px;
    line-height: 40px;
    letter-spacing: 1px;
  }
  .brand__dot {
    width: 18px;
    height: 18px;
    border-radius: 50%;
    background: var(--rose);
  }
  .ingredients {
    position: absolute;
    top: 120px;
    left: 0;
    width: 100%;
    text-align: center;
  }
  .ingredients__title {
    margin: 0;
    font-family: "Montserrat", sans-serif;
    font-weight: 700;
    font-size: 27px;
    line-height: 36px;
  }
  .ingredients__list {
    margin: 0;
    font-size: 31px;
    line-height: 38px;
    letter-spacing: -0.2px;
  }
  .description {
    position: absolute;
    top: 282px;
    left: 200px;
    width: 800px;
    margin: 0;
    text-align: center;
    font-size: 24px;
    line-height: 34px;
  }
  .facts__title {
    position: absolute;
    top: 402px;
    left: 0;
    width: 100%;
    margin: 0;
    text-align: center;
    font-family: "Montserrat", sans-serif;
    font-weight: 700;
    font-size: 35px;
    line-height: 44px;
    letter-spacing: -0.3px;
  }
  .facts__cell {
    position: absolute;
    background: var(--cell);
    box-shadow: 0 0 2px rgba(0,0,0,0.12);
    display: flex;
    align-items: center;
    justify-content: center;
    box-sizing: border-box;
  }
  .facts__head {
    top: 458px;
    height: 78px;
    font-size: 42px;
    color: var(--label-grey);
    white-space: nowrap;
    border-top: 6px solid var(--accent);
  }
  .facts__value {
    top: 547px;
    height: 154px;
    font-family: "Montserrat", sans-serif;
    font-weight: 700;
    font-size: 88px;
    color: var(--figure-grey);
    letter-spacing: -1px;
  }
  .facts__value--fat { padding-top: 20px; }
  .facts__value--carb { padding-bottom: 12px; }
  .facts__value--fiber { padding-bottom: 12px; padding-right: 30px; }
  .facts__value--cal {
    font-family: "Questrial", sans-serif;
    font-weight: 400;
    font-size: 54px;
    letter-spacing: -1px;
  }
  .col-fat { left: 168px; width: 227px; --accent: var(--sky); }
  .col-carb { left: 406px; width: 262px; --accent: var(--lime); }
  .col-fiber { left: 678px; width: 262px; --accent: var(--peach); }
  .col-cal { left: 951px; width: 101px; --accent: var(--lilac); }
  .origin {
    position: absolute;
    top: 856px;
    left: 0;
    width: 100%;
    margin: 0;
    text-align: center;
    font-size: 42px;
    line-height: 52px;
  }
</style>
</head>
<body>
  <main class="label">
    <div class="label__backdrop" role="img" aria-label="Photograph of a heap of whole raw almonds, softly faded"></div>
    <div class="label__band label__band--top"></div>

    <h1 class="brand"><span class="brand__dot"></span>PEBBLEWICK · ALMOND BUTTER</h1>

    <section class="ingredients">
      <h2 class="ingredients__title">INGREDIENTS:</h2>
      <p class="ingredients__list">ROASTED ALMONDS, ORGANIC CANE SUGAR,<br>PALM FRUIT OIL, SEA SALT</p>
    </section>

    <p class="description">Kernels from every far corner – stirred in Zurich. Slow-roasted almonds, ground small-batch into a creamy spread. Stir, scoop, repeat.</p>

    <section class="facts">
      <h2 class="facts__title">Nutritional Facts:</h2>

      <div class="facts__cell facts__head col-fat">Total Fat</div>
      <div class="facts__cell facts__head col-carb">Total Carb</div>
      <div class="facts__cell facts__head col-fiber">Dietary Fiber</div>
      <div class="facts__cell facts__head col-cal">Cal</div>

      <div class="facts__cell facts__value facts__value--fat col-fat">24%</div>
      <div class="facts__cell facts__value facts__value--carb col-carb">44%</div>
      <div class="facts__cell facts__value facts__value--fiber col-fiber">14%</div>
      <div class="facts__cell facts__value facts__value--cal col-cal">140</div>
    </section>

    <p class="origin">MADE IN SWITZERLAND</p>
    <div class="label__band label__band--bottom"></div>
  </main>
</body>
</html>
```